I have a logo and need to design the business card and stationery.
Updates

The uploaded logo image named as GREYHAVEN CONSTRUCTION which is to be replaced to GREYHAVEN CONTRACTS. Kindly add below details and submit the designs- Company name- Greyhaven Engineering Contracts LLP Name & Post- Kunal Mehra (Designated Partner) Address- Block No.317, Wing C, Tulsi Trade Plaza, Lokhand Marg, Varun Industrial Park, Goregaon(E), Mumbai - 400 063 Contact- +91 97410 58723 Email- kunalmehra@examplemail.com Website- www.greyhavencontracts.example Contact for Letterhead- +91-22-28145597

Hi Tanvir Rahman, We are liking your Design #41927506. We have suggested some changes which are mentioned in feedback. Kindly revert with it asap to finalize this design.

Colors

Designer to choose colors to be used in the design.

```html
<!DOCTYPE html>
<html lang="en">
<head>
<meta charset="utf-8">
<title>Greyhaven Contracts Letterhead</title>
<link href="https://fonts.googleapis.com/css2?family=Arimo:wght@400&family=Jost:wght@500;600&display=swap" rel="stylesheet">
<style>
:root{
  --backdrop:#d6d6d6;
  --paper:#fbfbfb;
  --ink:#505050;
  --ink-soft:#6a6a6a;
  --charcoal:#303133;
  --slate:#6c6c6c;
  --rule:#8a8a8a;
  --sign:#d9d9d9;
}
*{margin:0;padding:0;box-sizing:border-box}
html,body{width:1200px;height:1079px;overflow:hidden}
body{background:var(--backdrop);position:relative;font-family:"Arimo",Arial,sans-serif;color:var(--ink)}
.letterhead{position:absolute;left:268px;top:70px;width:664px;height:940px;background:var(--paper);overflow:hidden}
.brand{position:absolute;left:58px;top:48px;width:146px;text-align:center}
.brand-mark{width:30px;height:30px;background:var(--charcoal);margin:0 auto 8px}
.brand-name{font-family:"Jost",sans-serif;font-weight:600;font-size:12.5px;line-height:14px;letter-spacing:.5px;color:var(--charcoal)}
.divider{position:absolute;top:70px;width:1px;height:45px;background:var(--rule)}
.divider.first{left:228px}
.divider.second{left:434px}
.address{position:absolute;left:251px;top:67px;font-size:9.6px;line-height:12.1px;color:var(--ink-soft)}
.contacts{position:absolute;left:460px;top:74px;list-style:none;font-size:9.6px;color:var(--ink-soft)}
.contacts li{display:flex;align-items:center;height:14.2px}
.contacts svg{width:7px;height:7px;margin-right:3.5px;fill:var(--charcoal)}
.salutation{position:absolute;left:60px;top:288px;font-family:"Jost",sans-serif;font-weight:600;font-size:15.5px;color:var(--ink)}
.body-copy{position:absolute;left:59px;top:333px;width:550px;font-size:10.7px;line-height:13.7px;color:var(--ink)}
.body-copy p{margin-bottom:12.3px}
.closing{position:absolute;left:60px;top:608px;font-family:"Jost",sans-serif;font-weight:600;font-size:8.5px;color:var(--ink)}
.signature{position:absolute;left:59px;top:652px;width:110px;height:34px;background:var(--sign)}
.footer-wave{position:absolute;left:0;bottom:0;width:664px;height:80px}
</style>
</head>
<body>
<article class="letterhead">
  <header>
    <div class="brand">
      <div class="brand-mark"></div>
      <div class="brand-name">GREYHAVEN<br>CONTRACTS</div>
    </div>
    <span class="divider first"></span>
    <address class="address" style="font-style:normal">
      Block No.317, Wing C<br>
      Tulsi Trade Plaza, Lokhand Marg<br>
      Varun Industrial Park<br>
      Goregaon(E), Mumbai - 400 063
    </address>
    <span class="divider second"></span>
    <ul class="contacts">
      <li><svg viewBox="0 0 10 10"><path d="M2 0.5 L3.8 2.6 L2.9 3.6 Q4 6 6.4 7.1 L7.4 6.2 L9.5 8 L8.3 9.5 Q3.5 9 0.5 1.7Z"/></svg>+91-22-28145597</li>
      <li><svg viewBox="0 0 10 10"><path d="M0 2 H10 V8 H0Z M0.6 2.5 L5 5.8 L9.4 2.5" stroke="#fbfbfb" stroke-width=".8"/></svg>kunalmehra@examplemail.com</li>
      <li><svg viewBox="0 0 10 10"><circle cx="5" cy="5" r="5"/><path d="M0 5 H10 M5 0 V10" stroke="#fbfbfb" stroke-width=".8"/></svg>www.greyhavencontracts.example</li>
    </ul>
  </header>

  <h1 class="salutation">Dear Mr. Joshi,</h1>

  <section class="body-copy">
    <p>Lorem ipsum dolor sit amet, consectetuer adipiscing elit, sed diam nonmmy nibh euismod tincidunt ut laor eet dolore magna aliquam erat volutpat. Ut wisi enim ad minim veniam, quis nostrud exerci tationmcorper suscipit lobortis nisl ut aliquip ex ea commodo consequat. Duis autem vel eum iriure dolor in hendrerit in vulputate velit esse molestie consequat, vel illum dolore eu feugiat</p>
    <p>Rorem ipsum dolor sit amet, consectetuer adipiscing elit, sed diam nonmmy nibh euismod tincidunt ut laor eet dolore magna aliquam erat volutpat. Ut wisi enim ad minim veniam, quis nostrud exerci tationmcorper suscipit lobortis nisl ut aliquip ex ea commodo consequat. Duis autem vel eum iriure dolor in hendrerit in vulputate velit esse molest</p>
    <p>Dorem ipsum dolor sit amet, consectetuer adipiscing elit, sed diam nonmmy nibh euismod tincidunt ut laor eet dolore magna aliquam erat volutpat. Ut wisi enim ad minim veniam, quis nostrud exerci tationmcorper suscipit lobortis nisl ut aliquip ex ea commodo consequat. Duis autem vel eum iriure dolor in hendrerit in suscipit lobortis nisl ut aliquip ex ea commodo consequat. Duis autem vel eum iriure dolor in hendrerit in vulputate velit esse molestie consequat, vel illum</p>
    <p>Sorem ipsum dolor sit amet, consectetuer adipiscing elit, sed diam nonmmy nibh euismod tincidunt ut laor eet dolore magna aliquam erat volutpat. Ut wisi enim ad minim veniam, quis nostrud exerci tationmcorper suscipit lobortis nisl ut aliquip ex ea commodo consequat. Duis autem vel eum iriure dolor in</p>
  </section>

  <p class="closing">Sincerely,</p>
  <div class="signature" role="img" aria-label="Handwritten signature of the sender"></div>

  <svg class="footer-wave" viewBox="0 0 664 80" preserveAspectRatio="none" aria-hidden="true">
    <path d="M0 19 Q200 55 450 64 Q200 62 0 30Z" fill="var(--slate)"/>
    <path d="M0 47 Q330 95 664 38 L664 80 L0 80Z" fill="var(--charcoal)"/>
  </svg>
</article>
</body>
</html>
```